Cloud Based Internet Protection Service Business Cards

I would like a professionally designed business card. I already have a logo which I have attached.

The business is an online cloud based internet protection service aimed parents, particularly at non-technical parents and also schools.

The card should be be quite simple in its design, not to full of text and give its information in a clear and concise manner

Target Market(s)

Parents (especially non-technical parents) and also schools

Industry/Entity Type

Internet

Colors

Designer to choose colors to be used in the design.

Requirements
Should not have
• Too much text or be too cluttered. No decorative fonts, just a clear and concise font.

```html
<!DOCTYPE html>
<html lang="en">
<head>
<meta charset="utf-8">
<title>Harborly Net – Business Cards</title>
<link href="https://fonts.googleapis.com/css2?family=Arimo:wght@400;700&display=swap" rel="stylesheet">
<style>
  :root {
    --stage: #2e2c2a;
    --card-black: #0d0d0d;
    --card-black-edge: #262626;
    --brand-blue: #3f9fd6;
    --brand-deep: #1f5f86;
    --paper: #ffffff;
    --paper-grey: #d9d9d9;
    --ink: #333333;
    --ink-soft: #4a4a4a;
    --dark-card: #2a2a2a;
    --dark-box: #262626;
    --light-ink: #e6e6e6;
  }
  * { box-sizing: border-box; margin: 0; padding: 0; }
  html, body { width: 1200px; height: 900px; overflow: hidden; }
  body {
    background: var(--stage);
    font-family: "Arimo", Arial, sans-serif;
    position: relative;
  }
  .card { position: absolute; overflow: hidden; }

  /* Brand name lockup */
  .brand { position: absolute; display: flex; align-items: center; }
  .brand-dot { border-radius: 50%; flex: none; }
  .brand-name { font-weight: 700; letter-spacing: 0.04em; white-space: nowrap; }

  /* Large front */
  .front-large {
    left: 40px; top: 28px; width: 742px; height: 410px;
    background: radial-gradient(ellipse at 50% 40%, var(--card-black-edge), var(--card-black) 75%);
  }
  .front-large .brand { left: 0; right: 0; top: 0; bottom: 40px; justify-content: center; gap: 26px; }
  .front-large .brand-dot { width: 60px; height: 60px; background: var(--brand-blue); }
  .front-large .brand-name { font-size: 70px; color: var(--brand-blue); }

  /* Large back */
  .back-large {
    left: 40px; top: 460px; width: 742px; height: 410px;
    background: var(--paper);
    border: 1px solid #bdbdbd;
  }
  .back-pattern {
    position: absolute; left: 22px; top: 22px; width: 698px; height: 366px;
    background: linear-gradient(100deg, #c9c9c9 0%, #b5b5b5 60%, #d6d6d6 100%);
  }
  .back-heading {
    position: absolute; left: 38px; top: 40px; width: 480px; height: 66px;
    background: var(--paper); color: var(--ink);
    font-size: 24px; line-height: 30px; padding: 4px 10px;
  }
  .back-body {
    position: absolute; left: 38px; top: 132px; width: 370px; height: 168px;
    background: var(--paper); color: var(--ink);
    font-size: 17px; line-height: 22px; padding: 6px 12px;
  }
  .back-body .intro { text-align: justify; }
  .back-body .person { margin-top: 18px; font-weight: 700; font-size: 18px; }
  .back-large .brand { left: 44px; top: 320px; gap: 12px; }
  .back-large .brand-dot { width: 30px; height: 30px; background: var(--ink); }
  .back-large .brand-name { font-size: 34px; color: var(--ink); }

  /* Small light front */
  .front-small {
    left: 800px; top: 458px; width: 360px; height: 200px;
    background: linear-gradient(180deg, var(--paper) 0%, var(--paper-grey) 100%);
  }
  .front-small .brand { left: 0; right: 0; top: 0; bottom: 0; justify-content: center; gap: 12px; }
  .front-small .brand-dot { width: 28px; height: 28px; background: var(--brand-deep); }
  .front-small .brand-name { font-size: 34px; color: var(--brand-deep); }

  /* Small dark back */
  .back-small {
    left: 800px; top: 670px; width: 360px; height: 200px;
    background: var(--dark-card);
  }
  .back-small .back-pattern {
    left: 11px; top: 11px; width: 338px; height: 178px;
    background: linear-gradient(100deg, #4a4a4a 0%, #3a3a3a 60%, #505050 100%);
  }
  .back-small .back-heading {
    left: 8px; top: 9px; width: 232px; height: 32px;
    background: var(--dark-box); color: var(--light-ink);
    font-size: 12px; line-height: 14px; padding: 2px 5px;
  }
  .back-small .back-body {
    left: 8px; top: 52px; width: 180px; height: 82px;
    background: var(--dark-box); color: var(--light-ink);
    font-size: 8.5px; line-height: 10.5px; padding: 3px 6px;
  }
  .back-small .back-body .person { margin-top: 9px; font-size: 9px; }
  .back-small .brand { left: 20px; top: 157px; gap: 6px; }
  .back-small .brand-dot { width: 14px; height: 14px; background: var(--light-ink); }
  .back-small .brand-name { font-size: 16px; color: var(--light-ink); }
</style>
</head>
<body>

  <section class="card front-large" aria-label="Card front">
    <div class="brand">
      <span class="brand-dot"></span>
      <span class="brand-name">HARBORLY NET</span>
    </div>
  </section>

  <section class="card back-large" aria-label="Card back">
    <div class="back-pattern" role="img" aria-label="Diagonal line pattern with a silhouette of a parent and child holding hands"></div>
    <div class="back-pattern" style="background:none">
      <h2 class="back-heading" style="font-weight:400">CLOUD BASED<br>INTERNET PROTECTION SERVICE</h2>
      <div class="back-body">
        <p class="intro">We provide a safe and secure internet that is easy to implement for your professional and personal use.</p>
        <p class="person">Dana Whitfield</p>
        <p>0700 123 4567</p>
        <p>dana@harborly.example &nbsp;-&nbsp; harborly.example</p>
      </div>
    </div>
    <div class="brand">
      <span class="brand-dot"></span>
      <span class="brand-name">HARBORLY NET</span>
    </div>
  </section>

  <section class="card front-small" aria-label="Card front, light version">
    <div class="brand">
      <span class="brand-dot"></span>
      <span class="brand-name">HARBORLY NET</span>
    </div>
  </section>

  <section class="card back-small" aria-label="Card back, dark version">
    <div class="back-pattern" role="img" aria-label="Diagonal line pattern with a silhouette of a parent and child holding hands"></div>
    <div class="back-pattern" style="background:none">
      <h2 class="back-heading" style="font-weight:400">CLOUD BASED<br>INTERNET PROTECTION SERVICE</h2>
      <div class="back-body">
        <p class="intro">We provide a safe and secure internet that is easy to implement for your professional and personal use.</p>
        <p class="person">Dana Whitfield</p>
        <p>0700 123 4567</p>
        <p>dana@harborly.example - harborly.example</p>
      </div>
    </div>
    <div class="brand">
      <span class="brand-dot"></span>
      <span class="brand-name">HARBORLY NET</span>
    </div>
  </section>

</body>
</html>
```